Stationery Design Project - Meridan-Vale

Business Cards
Size: 90mm x 55mm

Letterhead
Size: A4 - 210mm x 297mm

With Compliments Slip
Size: DL - 210mm x 99mm

Notepad
Size: 250mm x 140mm

Presentation Folder
Size: A4

Meridan-Vale
*Perth *Brisbane *Seoul *Hongkong

website: www.meridanvale.com.au (Currently live, but being replaced with new one)

Engineering and Technical recruitment company for the Mining, Oil & Gas, Construction & Engineering Sectors
Updates

Industry/Entity Type

Business

```html
<!DOCTYPE html>
<html lang="en">
<head>
<meta charset="utf-8">
<title>Meridan-Vale Business Card</title>
<link rel="stylesheet" href="https://fonts.googleapis.com/css2?family=Ubuntu:wght@300;400;500&display=swap">
<style>
  :root {
    --page: #e6eaed;
    --card: #ffffff;
    --brand-blue: #2b8dbd;
    --band-grey: #6d6e70;
    --ink: #2f3336;
    --ink-soft: #4a4f53;
    --wordmark: #5d666d;
  }
  * { margin: 0; padding: 0; box-sizing: border-box; }
  html, body {
    width: 1200px; height: 960px; overflow: hidden;
    background: var(--page);
    font-family: "Ubuntu", sans-serif;
    color: var(--ink);
  }
  .canvas { position: relative; width: 1200px; height: 960px; }

  .card {
    position: absolute;
    width: 540px; height: 330px;
    background: var(--card);
    box-shadow: 0 6px 18px rgba(30, 50, 60, 0.18);
    overflow: hidden;
  }
  .card--front { left: 110px; top: 100px; }
  .card--back  { left: 550px; top: 520px; }

  /* Front */
  .brand-mark {
    position: absolute; left: 30px; top: 46px; width: 200px;
    display: flex; flex-direction: column; align-items: center; gap: 16px;
  }
  .brand-mark__dot {
    width: 118px; height: 118px; border-radius: 50%;
    background: var(--brand-blue);
  }
  .brand-mark__name { font-weight: 300; font-size: 22px; color: var(--wordmark); }

  .person { position: absolute; left: 300px; top: 50px; width: 240px; }
  .person__name { font-size: 23px; font-weight: 400; color: var(--ink); line-height: 28px; }
  .person__role { font-size: 14px; color: var(--ink-soft); margin-top: 4px; line-height: 18px; }
  .person__rule { height: 2px; background: var(--brand-blue); margin-top: 8px; width: 240px; }

  .contacts { list-style: none; position: absolute; left: 300px; top: 134px; }
  .contacts li {
    display: flex; align-items: center; gap: 10px;
    font-size: 15px; line-height: 21px; color: var(--ink);
  }
  .contacts svg { width: 13px; height: 13px; fill: var(--brand-blue); flex: none; }

  .address {
    position: absolute; left: 303px; top: 204px;
    font-style: normal; font-size: 15px; line-height: 21px; color: var(--ink);
  }

  .front-base { position: absolute; left: 0; bottom: 0; width: 540px; height: 60px; }
  .front-base svg { display: block; }
  .front-base__url {
    position: absolute; left: 32px; bottom: 13px;
    font-size: 17px; color: #fff; letter-spacing: 0.2px;
  }

  /* Back */
  .back-brand {
    position: absolute; left: 56px; top: 88px;
    display: flex; align-items: center; gap: 26px;
  }
  .back-brand__dot { width: 92px; height: 92px; border-radius: 50%; background: var(--brand-blue); }
  .back-brand__name { font-weight: 300; font-size: 46px; color: var(--wordmark); letter-spacing: 1px; }
  .back-band {
    position: absolute; left: 0; bottom: 0; width: 100%; height: 56px;
    background: var(--brand-blue);
    display: flex; align-items: center; justify-content: center;
  }
  .back-band__cities {
    color: #fff; font-size: 15px; font-weight: 500; letter-spacing: 0.6px;
    margin-left: 80px;
  }
</style>
</head>
<body>
<main class="canvas">

  <section class="card card--front" aria-label="Business card front">
    <div class="brand-mark">
      <span class="brand-mark__dot"></span>
      <span class="brand-mark__name">Meridan-Vale</span>
    </div>

    <div class="person">
      <h1 class="person__name">Nadia Hollings</h1>
      <p class="person__role">Project Manager</p>
      <div class="person__rule"></div>
    </div>

    <ul class="contacts">
      <li>
        <svg viewBox="0 0 16 16" aria-hidden="true"><path d="M3 1l3 3-1.5 2c1 2 3 4 5 5L11.5 9.5l3 3-2 2.5C7 14 2 9 1 3z"/></svg>
        08 6120 4700
      </li>
      <li>
        <svg viewBox="0 0 16 16" aria-hidden="true"><path d="M4 1h8v4H4zM1 6h14v7h-3v2H4v-2H1zm4 5v3h6v-3z"/></svg>
        08 6120 4788
      </li>
      <li>
        <svg viewBox="0 0 16 16" aria-hidden="true"><path d="M1 3h14v10H1zm1.5 1.5v.4L8 9l5.5-4.1v-.4zM2.5 6.6v4.9h11V6.6L8 10.7z"/></svg>
        info@meridanvale.com.au
      </li>
    </ul>

    <address class="address">
      Suite 4, 212 Harlow Street<br>
      Kelmscott Park<br>
      Western Australia 6011
    </address>

    <div class="front-base">
      <svg width="540" height="60" viewBox="0 0 540 60" aria-hidden="true">
        <path d="M274 16 Q279 20 290 20 H540 V29 H290 Q279 29 273 24 Z" fill="var(--band-grey)"/>
        <path d="M0 10 H252 Q262 10 267 16 L272 23 Q277 29 290 29 H540 V60 H0 Z" fill="var(--brand-blue)"/>
      </svg>
      <span class="front-base__url">www.meridanvale.com.au</span>
    </div>
  </section>

  <section class="card card--back" aria-label="Business card back">
    <div class="back-brand">
      <span class="back-brand__dot"></span>
      <span class="back-brand__name">Meridan-Vale</span>
    </div>
    <div class="back-band">
      <p class="back-band__cities">Darwin • Adelaide • Busan • Taipei</p>
    </div>
  </section>

</main>
</body>
</html>
```